Hosted Phone Service

We provide hosted phone service for less than $19.00 per user/seat. For many offices this is less money than what they are paying for their traditional phone lines.

Phone Service

```html
<!DOCTYPE html>
<html lang="en">
<head>
<meta charset="utf-8">
<title>Nimbus Line – Hosted Phone Service Postcard</title>
<link rel="stylesheet" href="https://fonts.googleapis.com/css2?family=Lato:wght@400;700&family=Exo+2:wght@600;700&family=Michroma&family=Crimson+Text:wght@600;700&family=Arimo&display=swap">
<style>
  :root {
    --backdrop: #7c5027;
    --navy: #253b8e;
    --sky: #a9dcf7;
    --ink: #2a2a2a;
    --white: #ffffff;
    --rule: #9a9a9a;
  }
  * { box-sizing: border-box; margin: 0; padding: 0; }
  html, body { width: 907px; height: 1200px; overflow: hidden; }
  body { background: var(--backdrop); position: relative; font-family: "Lato", sans-serif; color: var(--ink); }

  .card { position: absolute; left: 119px; width: 671px; background: var(--white); overflow: hidden; box-shadow: 0 3px 8px rgba(0,0,0,.35); }
  .card--front { top: 44px; height: 519px; }
  .card--back { top: 629px; height: 521px; }
  .card__art { position: absolute; inset: 0; }
  .abs { position: absolute; }

  /* front */
  .brand { left: 30px; top: 72px; font-family: "Crimson Text", serif; font-weight: 600; font-size: 21px; color: var(--navy); display: flex; align-items: center; gap: 8px; }
  .brand__dot { width: 14px; height: 14px; border-radius: 50%; background: var(--navy); }
  .follow { left: 247px; top: 47px; font-size: 16px; color: var(--navy); display: flex; align-items: center; gap: 5px; }
  .follow__dot { width: 23px; height: 23px; border-radius: 50%; background: #111; }
  .headline { left: 18px; top: 132px; color: var(--white); }
  .headline__lead { font-family: "Crimson Text", serif; font-weight: 600; font-size: 30px; letter-spacing: .5px; line-height: 32px; }
  .headline__main { font-family: "Michroma", sans-serif; font-size: 18.5px; line-height: 34px; font-weight: 700; }
  .headline__price { font-weight: 700; font-size: 16px; color: var(--sky); margin-top: 4px; letter-spacing: .2px; }
  .pill { background: var(--navy); color: var(--white); font-family: "Crimson Text", serif; font-weight: 700; font-size: 17px; padding: 1px 14px 1px 19px; border-radius: 0 14px 14px 0; }
  .pill--services { left: 0; top: 248px; }
  .services { left: 16px; top: 290px; list-style: none; font-size: 15px; line-height: 23.5px; }
  .services li::before { content: ""; display: inline-block; width: 6px; height: 6px; border-radius: 50%; background: var(--navy); margin-right: 14px; vertical-align: middle; }
  .front-url { left: 0; right: 0; top: 482px; text-align: center; font-size: 15px; color: var(--ink); padding-right: 10px; }

  /* back */
  .pill--about { left: 0; top: 21px; }
  .about-text { left: 17px; top: 57px; width: 331px; font-family: "Arimo", sans-serif; font-size: 15px; line-height: 20px; color: #111; }
  .about-text span { display: block; text-align: justify; text-align-last: justify; white-space: nowrap; }
  .about-text span:last-child { text-align-last: left; }
  .savings { left: 19px; top: 219px; font-family: "Exo 2", sans-serif; font-weight: 600; font-size: 18px; line-height: 26px; color: var(--white); white-space: nowrap; }
  .contact__title { left: 19px; top: 314px; font-family: "Crimson Text", serif; font-weight: 700; font-size: 17px; color: var(--navy); }
  .contact { left: 19px; top: 343px; list-style: none; font-size: 16px; line-height: 25px; }
  .contact li { display: flex; align-items: center; gap: 17px; }
  .contact svg { width: 12px; height: 12px; fill: var(--navy); }
  .stamp { left: 571px; top: 43px; width: 71px; height: 87px; border: 1px solid var(--rule); }
  .address-line { left: 414px; width: 219px; border-top: 1px solid var(--rule); }
  .address-line--1 { top: 217px; }
  .address-line--2 { top: 249px; }
  .address-line--3 { top: 284px; }
</style>
</head>
<body>

<section class="card card--front" aria-label="Postcard front">
  <svg class="card__art" viewBox="0 0 671 519" width="671" height="519">
    <defs>
      <linearGradient id="photoOffice" x1="0" y1="0" x2="1" y2="1">
        <stop offset="0" stop-color="#eef1f4"/>
        <stop offset=".6" stop-color="#c9d2dc"/>
        <stop offset="1" stop-color="#dfe5ec"/>
      </linearGradient>
      <linearGradient id="photoHand" x1="0" y1="0" x2="0" y2="1">
        <stop offset="0" stop-color="#2a2a2a"/>
        <stop offset="1" stop-color="#e2bfa6"/>
      </linearGradient>
      <linearGradient id="darkBand" x1="0" y1="0" x2="1" y2="0">
        <stop offset="0" stop-color="#2a2a2a"/>
        <stop offset="1" stop-color="#5c5c5c"/>
      </linearGradient>
      <linearGradient id="footBand" x1="0" y1="0" x2="1" y2="0">
        <stop offset="0" stop-color="#9fd6f5"/>
        <stop offset=".5" stop-color="#d6effc"/>
        <stop offset="1" stop-color="#9fd6f5"/>
      </linearGradient>
    </defs>
    <line x1="0" y1="121" x2="430" y2="121" stroke="var(--sky)" stroke-width="3"/>
    <path d="M454,0 C470,90 420,200 340,290 L356,290 C440,200 488,90 470,0Z" fill="var(--sky)"/>
    <path d="M475,0 H671 V98 C580,110 500,170 440,250 C480,170 495,90 475,0Z" fill="var(--navy)"/>
    <path role="img" aria-label="Photo of a smiling office worker on a desk phone" d="M671,98 V462 H336 C360,330 420,230 500,170 C560,125 610,105 671,98Z" fill="url(#photoOffice)"/>
    <rect x="0" y="124" width="428" height="107" fill="url(#darkBand)"/>
    <path d="M0,428 C120,420 250,380 330,330 L336,340 C260,400 140,440 0,446Z" fill="var(--sky)"/>
    <path d="M0,446 C150,440 270,410 340,370 L336,462 H671 V470 H0Z" fill="var(--navy)"/>
    <rect role="img" aria-label="Photo of a hand holding a smartphone" x="262" y="256" width="110" height="212" rx="12" fill="url(#photoHand)"/>
    <rect x="0" y="474" width="671" height="45" fill="url(#footBand)"/>
  </svg>

  <div class="abs brand"><span class="brand__dot"></span>Nimbus Line</div>
  <div class="abs follow">Follow us on <span class="follow__dot"></span><span class="follow__dot"></span></div>

  <div class="abs headline">
    <p class="headline__lead">WE PROVIDE</p>
    <p class="headline__main">Hosted phone service</p>
    <p class="headline__price">FOR LESS THAN $19.00 PER USER/SEAT</p>
  </div>

  <div class="abs pill pill--services">Our Services</div>
  <ul class="abs services">
    <li>Lorem ipsum dolor sit amet</li>
    <li>Sectetuer adipiscing elit</li>
    <li>Commodo ligula eget</li>
    <li>Aenean vulputate</li>
  </ul>

  <p class="abs front-url">www.nimbusline.com</p>
</section>

<section class="card card--back" aria-label="Postcard back">
  <svg class="card__art" viewBox="0 0 671 521" width="671" height="521">
    <defs>
      <linearGradient id="aboutPanel" x1="0" y1="0" x2="1" y2="0">
        <stop offset="0" stop-color="#8fcdf2"/>
        <stop offset=".7" stop-color="#bfe5fa"/>
        <stop offset="1" stop-color="#8fcdf2"/>
      </linearGradient>
      <linearGradient id="savingsBand" x1="0" y1="0" x2="1" y2="0">
        <stop offset="0" stop-color="#252525"/>
        <stop offset="1" stop-color="#5a5a5a"/>
      </linearGradient>
    </defs>
    <path d="M0,0 H360 C384,120 390,300 338,429 H0Z" fill="url(#aboutPanel)"/>
    <path d="M346,0 H356 C392,130 396,300 344,429 H334 C384,300 380,130 346,0Z" fill="var(--navy)"/>
    <path d="M362,0 H368 C404,130 406,300 354,429 H348 C398,300 396,130 362,0Z" fill="#111"/>
    <path d="M0,214 H382 C381,245 377,275 370,304 H0Z" fill="url(#savingsBand)"/>
  </svg>

  <div class="abs pill pill--about">About Us</div>
  <p class="abs about-text">
    <span>Lorem ipsum dolor sit amet, consectetuer</span>
    <span>adipiscing elit. Aenean commodo ligula eget</span>
    <span>dolor. Aenean massa. Cum sociis natoque</span>
    <span>penatibus et magnis dis parturient montes,</span>
    <span>nascetur ridiculus mus. Donec quam felis,</span>
    <span>ultricies nec, pellentesque eu, pretium quis,</span>
    <span>sem. Nulla consequat massa quis enim.</span>
  </p>

  <p class="abs savings">For many offices this is less money<br>than what they are paying for their<br>traditional phone lines</p>

  <p class="abs contact__title">Contact us for more information</p>
  <ul class="abs contact">
    <li><svg viewBox="0 0 12 12"><path d="M2.5,0.5 L4.5,3 L3.3,4.4 C4,6 6,8 7.6,8.7 L9,7.5 L11.5,9.5 L10,11.5 C5,11 1,7 0.5,2Z"/></svg>0198765432</li>
    <li><svg viewBox="0 0 12 12"><rect x="1" y="2.5" width="10" height="7" rx="1"/><path d="M1.5,3 L6,6.5 L10.5,3" fill="none" stroke="#fff" stroke-width="1"/></svg>hello@nimbusline.com</li>
    <li><svg viewBox="0 0 12 12"><circle cx="6" cy="6" r="5"/><path d="M1,6 H11 M6,1 C3.5,4 3.5,8 6,11 M6,1 C8.5,4 8.5,8 6,11" fill="none" stroke="#fff" stroke-width=".8"/></svg>www.nimbusline.com</li>
  </ul>

  <div class="abs stamp"></div>
  <div class="abs address-line address-line--1"></div>
  <div class="abs address-line address-line--2"></div>
  <div class="abs address-line address-line--3"></div>
</section>

</body>
</html>
```